Redesign of Business Card to look more professional and stand out

Business card design. You can lean more about our company by going to dlmfabworks.example. Raised letters would be nice. Company name & Address
DL&M
418 Wrenfield Crest Drive, Suite 140
Birmingham, AL 35999

You can use my name and title: Glenn Marlowe
Business Development Manager

Target Market(s)

Heavy Industrial market, i.e. utilities, chemical plants, paper mills, construction companies

Industry/Entity Type

Construction

Contact Information for Business Card

We provide Project Management & Project Support Services

Font styles to use
Serif

Requirements
Must have
• Company name & Address
• DL&M
• 418 Wrenfield Crest Drive, Suite 140
• Birmingham, AL 35999
Nice to have
• ideas for the back of the card
Should not have
• no crazy colors. needs to look professional and standout.

```html
<!DOCTYPE html>
<html lang="en">
<head>
<meta charset="utf-8">
<title>DL&amp;M Business Card</title>
<link href="https://fonts.googleapis.com/css2?family=Arimo:wght@400;700&display=swap" rel="stylesheet">
<style>
  :root {
    --navy: #1f3b70;
    --navy-dark: #182f5c;
    --navy-light: #284a87;
    --white: #ffffff;
    --paper: #f7f7f7;
    --edge-grey: #c9ccd2;
    --backdrop: #e9e7e3;
  }
  * { box-sizing: border-box; margin: 0; padding: 0; }
  html, body {
    width: 1200px; height: 950px; overflow: hidden;
    background: var(--backdrop);
    font-family: "Arimo", Arial, sans-serif;
  }
  .canvas {
    width: 1200px; height: 950px;
    display: flex; flex-direction: column;
    align-items: center; justify-content: center; gap: 40px;
  }
  .card {
    position: relative;
    width: 720px; height: 411px;
    border-radius: 4px;
    overflow: hidden;
    box-shadow: 0 10px 28px rgba(0,0,0,.18);
  }

  /* Front */
  .card-front {
    background: linear-gradient(135deg, var(--navy-light) 0%, var(--navy) 45%, var(--navy-dark) 100%);
    color: var(--white);
  }
  .front-brand {
    position: absolute; left: 0; right: 0; top: 96px;
    display: flex; flex-direction: column; align-items: center;
  }
  .front-wordmark {
    font-weight: 700; font-size: 118px; line-height: 1;
    letter-spacing: 2px;
  }
  .front-url {
    margin-top: 10px;
    font-size: 15px; letter-spacing: 4px;
  }
  .front-tagline {
    position: absolute; left: 0; right: 0; bottom: 44px;
    text-align: center;
    font-weight: 700; font-size: 17px;
  }

  /* Back */
  .card-back { background: var(--paper); }
  .back-panel { position: absolute; inset: 0; }
  .back-details {
    position: absolute; left: 40px; top: 120px;
    color: var(--white);
  }
  .contact-name { font-weight: 700; font-size: 24px; }
  .contact-title { font-size: 17px; margin-top: 4px; }
  .contact-address { font-size: 17px; line-height: 1.3; margin-top: 16px; }
  .contact-list { list-style: none; margin-top: 10px; font-size: 17px; }
  .contact-list li { display: flex; align-items: center; gap: 10px; line-height: 1.4; }
  .contact-list svg { width: 15px; height: 15px; flex: none; }
  .back-wordmark {
    position: absolute; left: 430px; right: 0; top: 150px;
    text-align: center;
    font-weight: 700; font-size: 88px; line-height: 1;
    color: var(--navy);
    letter-spacing: 1px;
  }
</style>
</head>
<body>
<main class="canvas">

  <section class="card card-front" aria-label="Card front">
    <div class="front-brand">
      <div class="front-wordmark">DL&amp;M</div>
      <div class="front-url">www.dlmfabworks.example</div>
    </div>
    <p class="front-tagline">We provide Project Management &amp; Project Support Services</p>
  </section>

  <section class="card card-back" aria-label="Card back">
    <svg class="back-panel" viewBox="0 0 720 411" preserveAspectRatio="none" aria-hidden="true">
      <path d="M0 0 H318 Q352 0 360 34 V377 Q352 411 318 411 H0 Z" fill="var(--edge-grey)" transform="translate(8 0)"/>
      <path d="M0 0 H318 Q352 0 360 34 V377 Q352 411 318 411 H0 Z" fill="var(--navy)"/>
    </svg>

    <div class="back-details">
      <p class="contact-name">Glenn Marlowe</p>
      <p class="contact-title">Business Development Manager</p>
      <p class="contact-address">418 Wrenfield Crest Drive<br>Suite 140<br>Birmingham, AL 35999</p>
      <ul class="contact-list">
        <li>
          <svg viewBox="0 0 16 16"><path d="M2 6 Q8 1 14 6 L12 8 L10 6.5 H6 L4 8 Z M4 9 H12 L13 14 H3 Z" fill="#fff"/><circle cx="8" cy="11.3" r="1.4" fill="var(--navy)"/></svg>
          205-555-0163
        </li>
        <li>
          <svg viewBox="0 0 16 16"><rect x="4" y="1" width="8" height="14" rx="1.5" fill="none" stroke="#fff" stroke-width="1.6"/><circle cx="8" cy="12.5" r="0.9" fill="#fff"/></svg>
          205-555-0164
        </li>
        <li>
          <svg viewBox="0 0 16 16"><rect x="1" y="3" width="14" height="10" rx="1" fill="#fff"/><path d="M1.5 3.5 L8 9 L14.5 3.5" fill="none" stroke="var(--navy)" stroke-width="1.3"/></svg>
          glenn@dlmfabworks.example
        </li>
        <li>
          <svg viewBox="0 0 16 16"><circle cx="8" cy="8" r="7" fill="#fff"/><path d="M1 8 H15 M8 1 Q4 8 8 15 Q12 8 8 1" fill="none" stroke="var(--navy)" stroke-width="1.1"/></svg>
          www.dlmfabworks.example
        </li>
      </ul>
    </div>

    <div class="back-wordmark">DL&amp;M</div>
  </section>

</main>
</body>
</html>
```